Local Roofing Company Billboard Design

We need a billboard design for an 8' x 32' billboard. This billboard would need to be easily readable and stand out well.
I have uploaded a design that we like - simple, readable, and gets the point across. We do NOT want the $1000 off offer included.
We are looking for a black background with white copy so it will stand out. We want the following on the billboard:
Kessler Roofing logo
kessler-roofing.example (optional)
555.271.6384 (mandatory)
Photo is optional, depends on how it all lays out
Production file must comply with layout requirements (uploaded).
Target Market(s)
Homeowners
Font styles to use
Other font styles liked:
- match font from logo
Colors
Designer to choose colors to be used in the design.
Requirements
Must have
- Black background, white copy, logo must be large and legible. Colors used must match our logo colors.

```html
<!DOCTYPE html>
<html lang="en">
<head>
<meta charset="utf-8">
<title>Kessler Roofing Billboard</title>
<link href="https://fonts.googleapis.com/css2?family=Archivo+Black&family=Arvo:wght@700&display=swap" rel="stylesheet">
<style>
  :root {
    --ink: #000000;
    --paper: #ffffff;
    --accent: #e85a24;
    --stage: #eceef0;
  }
  html, body {
    margin: 0;
    padding: 0;
    width: 1200px;
    height: 1152px;
    overflow: hidden;
    background: var(--stage);
  }
  .billboard {
    position: absolute;
    left: 0;
    top: 426px;
    width: 1200px;
    height: 300px;
    background: var(--ink);
    overflow: hidden;
  }
  .billboard-shapes {
    position: absolute;
    inset: 0;
    width: 100%;
    height: 100%;
  }
  .brand-name {
    position: absolute;
    left: 0;
    right: 0;
    top: 62px;
    margin: 0;
    text-align: center;
    font-family: "Arvo", serif;
    font-weight: 700;
    font-size: 44px;
    line-height: 1;
    color: var(--paper);
  }
  .phone {
    position: absolute;
    left: 0;
    right: 0;
    top: 142px;
    display: flex;
    justify-content: center;
    align-items: center;
    gap: 18px;
    padding-left: 20px;
  }
  .phone-icon { width: 44px; height: 44px; }
  .phone-number {
    font-family: "Archivo Black", sans-serif;
    font-size: 68px;
    line-height: 1;
    color: var(--paper);
    letter-spacing: 1px;
  }
  .website {
    position: absolute;
    left: 0;
    right: 0;
    top: 232px;
    height: 38px;
    display: flex;
    justify-content: center;
    align-items: center;
    gap: 12px;
  }
  .globe-icon { width: 28px; height: 28px; }
  .website-url {
    font-family: "Arvo", serif;
    font-weight: 700;
    font-size: 31px;
    line-height: 1;
    color: var(--paper);
  }
</style>
</head>
<body>
  <section class="billboard">
    <svg class="billboard-shapes" viewBox="0 0 1960 490" preserveAspectRatio="none" aria-hidden="true">
      <!-- left corner bands -->
      <polygon points="0,0 430,0 180,125 0,125" fill="var(--accent)"/>
      <polygon points="0,125 180,125 430,0 670,0 190,240 0,240" fill="var(--paper)"/>
      <!-- right corner panel -->
      <polygon points="1170,0 1960,0 1960,330" fill="var(--paper)"/>
      <polygon points="1760,0 1830,0 1620,165 1565,132" fill="var(--ink)"/>
      <polygon points="1880,0 1960,0 1960,60 1900,120 1860,80" fill="var(--accent)"/>
      <polygon points="1650,210 1715,150 1830,265 1775,300" fill="var(--accent)"/>
      <!-- partner mark placeholder -->
      <rect class="partner-mark" x="1760" y="75" width="90" height="90" fill="var(--ink)"/>
      <!-- lower bands -->
      <polygon points="0,368 975,368 985,378 1960,378 1960,440 0,440" fill="var(--accent)"/>
      <polygon points="0,362 970,362 982,372 0,372" fill="var(--paper)"/>
      <polygon points="985,440 1960,440 1960,448 995,448" fill="var(--paper)"/>
    </svg>

    <h1 class="brand-name">Kessler Roofing</h1>

    <div class="phone">
      <svg class="phone-icon" viewBox="0 0 48 48" aria-hidden="true">
        <path d="M12 6 l7 9 -4 5 c2 5 6 9 11 12 l5 -4 9 7 -5 7 c-14 -1 -27 -14 -28 -29 z" fill="var(--accent)"/>
        <path d="M28 10 a12 12 0 0 1 10 10" stroke="var(--accent)" stroke-width="3" fill="none" stroke-linecap="round"/>
        <path d="M28 3 a19 19 0 0 1 17 17" stroke="var(--accent)" stroke-width="3" fill="none" stroke-linecap="round"/>
      </svg>
      <span class="phone-number">555-271-6384</span>
    </div>

    <div class="website">
      <svg class="globe-icon" viewBox="0 0 32 32" aria-hidden="true">
        <circle cx="14" cy="14" r="11" fill="none" stroke="var(--ink)" stroke-width="2"/>
        <ellipse cx="14" cy="14" rx="5" ry="11" fill="none" stroke="var(--ink)" stroke-width="2"/>
        <line x1="3" y1="14" x2="25" y2="14" stroke="var(--ink)" stroke-width="2"/>
        <path d="M20 18 l10 5 -4 1 3 5 -2 1 -3 -5 -3 3 z" fill="var(--ink)"/>
      </svg>
      <span class="website-url">kessler-roofing.example</span>
    </div>
  </section>
</body>
</html>
```